Loomtide - agency page

We are a full service digital agency. Design, development, marketing and SEO/content - but we haven’t got time for our own page. Site looks now like a one pager with just text. We want to keep the colors we got, and the logo stays the same. The site is https://loomtide.no. We need at least a frontpage and an article page. Archive is nice to have.

We are also need more designers for client projects, so there might be more work here.

```html
<!DOCTYPE html>
<html lang="en">
<head>
<meta charset="utf-8">
<title>Loomtide – Full service digital agency</title>
<link rel="stylesheet" href="https://fonts.googleapis.com/css2?family=Inter:wght@400;500;600;700&family=Playfair+Display:wght@500&display=swap">
<style>
  :root {
    --frame: #3b1858;
    --hero-top: #5b2e80;
    --hero-bottom: #3e1966;
    --lilac-band: #ddd2ec;
    --ink-light: #efe4f7;
    --ink-muted: #b59bd0;
    --accent: #8f3fd0;
    --accent-deep: #4a1d6e;
    --icon-soft: #9b64c9;
    --feature-ink: #3e2156;
    --feature-text: #b6a5cc;
    --art-a: #7c4aae;
    --art-b: #c9b3e6;
  }
  * { box-sizing: border-box; margin: 0; padding: 0; }
  html, body { width: 1200px; height: 800px; overflow: hidden; }
  body {
    background: var(--frame);
    font-family: "Inter", sans-serif;
    position: relative;
  }
  .page {
    position: absolute; left: 37px; top: 6px; width: 1125px; height: 783px;
    background: linear-gradient(180deg, var(--hero-top) 0%, var(--hero-bottom) 65%);
    overflow: hidden;
  }
  .wave { position: absolute; left: 0; top: 460px; width: 1125px; height: 323px; }

  .brand { position: absolute; left: 156px; top: 47px; text-align: center; }
  .brand-name { font-size: 14px; font-weight: 600; letter-spacing: 1.5px; color: var(--ink-light); }
  .brand-tag { font-size: 5px; letter-spacing: 0.6px; color: var(--ink-muted); margin-top: 3px; }

  .nav { position: absolute; top: 47px; left: 0; }
  .nav a {
    position: absolute; top: 0; font-size: 8px; font-weight: 500; letter-spacing: 0.6px;
    color: var(--ink-muted); text-decoration: none; text-transform: uppercase; white-space: nowrap;
  }
  .nav-cta {
    position: absolute; left: 967px; top: 37px; width: 96px; height: 27px; border-radius: 14px;
    background: var(--accent); color: var(--ink-light); font-size: 8px; font-weight: 600;
    display: flex; align-items: center; justify-content: center; text-transform: uppercase; letter-spacing: 0.5px;
  }

  .hero-title {
    position: absolute; left: 139px; top: 132px;
    font-family: "Playfair Display", serif; font-weight: 500; font-size: 45px; line-height: 48px;
    color: var(--ink-light);
  }
  .hero-text {
    position: absolute; left: 146px; top: 260px; width: 325px;
    font-size: 8.5px; line-height: 12px; color: var(--ink-muted);
  }
  .hero-cta {
    position: absolute; left: 140px; top: 326px; width: 104px; height: 39px; border-radius: 20px;
    background: var(--accent); color: var(--ink-light); font-size: 9px; font-weight: 600;
    display: flex; align-items: center; justify-content: center; text-transform: uppercase; letter-spacing: 0.4px;
  }
  .hero-art {
    position: absolute; left: 390px; top: 164px; width: 720px; height: 290px; border-radius: 24px;
    background: radial-gradient(ellipse at 55% 45%, var(--art-b) 0%, var(--art-a) 55%, rgba(124,74,174,0) 78%);
  }

  .features { position: absolute; left: 0; top: 0; width: 1200px; }
  .feature { position: absolute; top: 599px; width: 150px; margin-left: -75px; text-align: center; }
  .feature-icon {
    width: 44px; height: 44px; border-radius: 50%; background: var(--icon-soft);
    margin: 0 auto; display: flex; align-items: center; justify-content: center;
  }
  .feature-icon.is-active { background: var(--accent-deep); }
  .feature-title { margin-top: 14px; font-size: 10px; font-weight: 700; color: var(--feature-ink); }
  .feature-text { margin: 16px auto 0; width: 142px; font-size: 7px; line-height: 12px; color: var(--feature-text); text-align: left; }
</style>
</head>
<body>
  <main class="page">
    <svg class="wave" viewBox="0 0 1125 323" preserveAspectRatio="none" aria-hidden="true">
      <path d="M0 53 C 180 80, 360 30, 560 20 C 760 10, 900 30, 1125 -12 L1125 323 L0 323 Z" fill="var(--lilac-band)"/>
    </svg>
  </main>

  <div class="brand">
    <div class="brand-name">LOOMTIDE</div>
    <div class="brand-tag">FULL SERVICE DIGITAL AGENCY</div>
  </div>

  <nav class="nav">
    <a style="left:687px">Services</a>
    <a style="left:776px">Work</a>
    <a style="left:887px">About</a>
  </nav>
  <div class="nav-cta">Contact</div>

  <h1 class="hero-title">Crafting<br>Digital Sites</h1>
  <p class="hero-text">We design, build and grow websites for brands that want to stand out. From strategy and identity to code, marketing and content, our team handles every step so you can focus on your business.</p>
  <div class="hero-cta">Get started</div>

  <div class="hero-art" role="img" aria-label="Illustration of website cards, a clock, a rising bar chart and leafy plants in purple tones"></div>

  <section class="features">
    <div class="feature" style="left:217px">
      <div class="feature-icon"><svg width="18" height="12" viewBox="0 0 18 12"><path d="M2 2h14M2 6h14M2 10h14" stroke="#efe4f7" stroke-width="2"/></svg></div>
      <h3 class="feature-title">Strategic Brand</h3>
      <p class="feature-text">Positioning, identity and voice shaped around your goals and the people you serve.</p>
    </div>
    <div class="feature" style="left:404px">
      <div class="feature-icon"><svg width="14" height="12" viewBox="0 0 14 12"><rect x="1" y="1" width="12" height="10" rx="2" fill="#efe4f7"/></svg></div>
      <h3 class="feature-title">Creative Design</h3>
      <p class="feature-text">Interfaces and visuals that feel clear, modern and easy to use on every screen.</p>
    </div>
    <div class="feature" style="left:598px">
      <div class="feature-icon is-active"><svg width="16" height="16" viewBox="0 0 16 16"><circle cx="7" cy="7" r="4.5" fill="none" stroke="#efe4f7" stroke-width="2"/><path d="M10.5 10.5 14 14" stroke="#efe4f7" stroke-width="2"/></svg></div>
      <h3 class="feature-title">Market and Search</h3>
      <p class="feature-text">Campaigns and SEO that bring the right visitors and turn them into real clients.</p>
    </div>
    <div class="feature" style="left:785px">
      <div class="feature-icon"><svg width="16" height="12" viewBox="0 0 16 12"><path d="M5 2 1 6l4 4M11 2l4 4-4 4" fill="none" stroke="#efe4f7" stroke-width="2"/></svg></div>
      <h3 class="feature-title">Coding Work</h3>
      <p class="feature-text">Fast, stable sites built with clean code and tools your team can manage.</p>
    </div>
    <div class="feature" style="left:961px">
      <div class="feature-icon"><svg width="14" height="14" viewBox="0 0 14 14"><path d="M2 12 3 8l7-7 3 3-7 7z" fill="#efe4f7"/></svg></div>
      <h3 class="feature-title">Content Services</h3>
      <p class="feature-text">Articles, guides and stories written to inform readers and rank well over time.</p>
    </div>
  </section>
</body>
</html>
```